Valbrina Soletti Winery 2023 Label

We are just about to bottle our very first Napa Valley Cabernet Sauvignon and need label ideas

Target Market(s)

Cab drinkers who like Napa California Cabs

Industry/Entity Type

Wine Making

Logo Text

Valbrina Soletti 2023 Napa Estate Grown Cabernet Sauvignon

Requirements
Must have
• Winery Name, year of vintage and Napa Estate Cab
Nice to have
• If using the initials V and S use gold letters on black or red background

```html
<!DOCTYPE html>
<html lang="en">
<head>
<meta charset="utf-8">
<title>Valbrina Soletti Vineyards – Estate Cabernet Sauvignon</title>
<link rel="stylesheet" href="https://fonts.googleapis.com/css2?family=Bodoni+Moda:wght@500&family=Josefin+Sans:wght@400&display=swap">
<style>
  :root {
    --label-black: #1b1b1b;
    --label-black-deep: #141414;
    --gold: #e8c697;
    --silver: #a8a8a8;
  }
  html, body {
    margin: 0;
    padding: 0;
    width: 989px;
    height: 1200px;
    overflow: hidden;
    background: var(--label-black);
  }
  .label {
    position: relative;
    width: 989px;
    height: 1200px;
    background: radial-gradient(ellipse at 50% 45%, var(--label-black) 0%, var(--label-black-deep) 100%);
    overflow: hidden;
  }
  .label__frame {
    position: absolute;
    left: 35px;
    top: 36px;
    right: 35px;
    bottom: 36px;
    border: 2.5px solid var(--gold);
  }
  .winery-name {
    position: absolute;
    left: 0;
    right: 0;
    top: 118px;
    margin: 0;
    text-align: center;
    font-family: "Bodoni Moda", "Didot", serif;
    font-weight: 500;
    font-size: 62px;
    line-height: 92px;
    letter-spacing: 4px;
    color: var(--silver);
    transform: scaleX(0.78);
    transform-origin: 50% 0;
    white-space: nowrap;
  }
  .winery-name__line {
    display: block;
  }
  .brand-mark {
    position: absolute;
    left: 0;
    right: 0;
    top: 520px;
    text-align: center;
    font-family: "Bodoni Moda", "Didot", serif;
    font-weight: 500;
    font-size: 64px;
    line-height: 84px;
    letter-spacing: 3px;
    color: var(--gold);
  }
  .brand-mark__line {
    display: block;
  }
  .varietal {
    position: absolute;
    left: 0;
    right: 0;
    top: 886px;
    margin: 0;
    text-align: center;
    font-family: "Josefin Sans", "Futura", sans-serif;
    font-weight: 400;
    font-size: 33px;
    letter-spacing: 4.2px;
    color: var(--silver);
    white-space: nowrap;
  }
  .appellation,
  .vintage {
    position: absolute;
    left: 0;
    right: 0;
    margin: 0;
    text-align: center;
    font-family: "Josefin Sans", "Futura", sans-serif;
    font-weight: 400;
    font-size: 32px;
    letter-spacing: 8px;
    color: var(--silver);
  }
  .appellation { top: 980px; }
  .vintage { top: 1018px; }
</style>
</head>
<body>
  <main class="label">
    <div class="label__frame"></div>

    <h1 class="winery-name">
      <span class="winery-name__line">VALBRINA SOLETTI</span>
      <span class="winery-name__line">VINEYARDS</span>
    </h1>

    <div class="brand-mark" aria-label="Valbrina Soletti">
      <span class="brand-mark__line">VALBRINA</span>
      <span class="brand-mark__line">SOLETTI</span>
    </div>

    <p class="varietal">ESTATE CABERNET SAUVIGNON</p>
    <p class="appellation">NAPA</p>
    <p class="vintage">2025</p>
  </main>
</body>
</html>
```